Need a new letterhead

Need a new fresh exciting letterhead. Remove the footer...info is outdated.

Target Market(s)

B2B

Industry/Entity Type

Electrical Power

Colors

Designer to choose colors to be used in the design.

Requirements
Must have
• Red and Blue Corvane Systems Logo
Nice to have
• POWERING A BRIGHTER, CLEANER TOMORROW in footer...reorganize the words?

```html
<!DOCTYPE html>
<html lang="en">
<head>
<meta charset="utf-8">
<title>Corvane Systems Letterhead</title>
<link href="https://fonts.googleapis.com/css2?family=Arimo:wght@400;700&display=swap" rel="stylesheet">
<style>
  :root {
    --brand-red: #ee0220;
    --brand-blue: #142e8c;
    --paper: #ffffff;
    --backdrop: #cfcfcf;
    --watermark: #fbeef0;
  }
  html, body {
    margin: 0;
    padding: 0;
    width: 1200px;
    height: 1200px;
    overflow: hidden;
    background: var(--backdrop);
  }
  .letterhead {
    position: absolute;
    left: 203px;
    top: 40px;
    width: 793px;
    height: 1120px;
    display: block;
    overflow: hidden;
    background: var(--paper);
  }
  .letterhead text {
    font-family: "Arimo", Arial, sans-serif;
  }
  .band-red { fill: var(--brand-red); }
  .band-blue { fill: var(--brand-blue); }
  .sheet { fill: var(--paper); }
  .logo-plate { fill: var(--paper); }
  .logo-name { fill: var(--brand-red); font-weight: 700; font-size: 27px; }
  .tagline { fill: var(--paper); font-size: 20px; letter-spacing: 1.4px; }
  .watermark-name { fill: var(--watermark); font-weight: 700; font-size: 124px; }
  .contact-text { fill: var(--paper); font-size: 17px; }
  .icon { fill: var(--paper); }
  .icon-line { fill: none; stroke: var(--paper); stroke-width: 2; }
</style>
</head>
<body>
<svg class="letterhead" viewBox="0 0 1143 1615" xmlns="http://www.w3.org/2000/svg" aria-label="Corvane Systems letterhead">
  <rect class="sheet" x="-10" y="-10" width="1163" height="1635"/>

  <!-- header bands -->
  <rect class="band-red" x="-10" y="-10" width="1163" height="310"/>
  <path class="band-blue" d="M520,152 C750,140 950,134 1153,133 L1153,300 L520,300 Z"/>
  <path class="sheet" d="M-10,246 C200,170 430,152 560,150 C820,152 1040,185 1153,230 L1153,1400 L-10,1400 Z"/>

  <!-- logo name -->
  <rect class="logo-plate" x="33" y="46" width="210" height="105" rx="12"/>
  <text class="logo-name" x="138" y="92" text-anchor="middle">Corvane</text>
  <text class="logo-name" x="138" y="124" text-anchor="middle">Systems</text>

  <text class="tagline" x="1115" y="78" text-anchor="end">POWERING A BRIGHTER, CLEANER TOMORROW</text>

  <!-- faint name mark -->
  <text class="watermark-name" x="572" y="760" text-anchor="middle">CORVANE</text>
  <text class="watermark-name" x="572" y="930" text-anchor="middle">SYSTEMS</text>

  <!-- footer bands -->
  <path class="band-blue" d="M-10,1387 C200,1440 450,1462 620,1465 C400,1478 200,1483 -10,1483 Z"/>
  <path class="band-red" d="M-10,1483 C200,1483 400,1478 620,1465 C850,1450 1050,1410 1153,1371 L1153,1625 L-10,1625 Z"/>

  <!-- contact: address -->
  <path class="icon" d="M50,1536 a12,12 0 0 1 12,12 c0,9 -12,22 -12,22 c0,0 -12,-13 -12,-22 a12,12 0 0 1 12,-12 z M50,1543 a5,5 0 1 0 0.01,0 z" fill-rule="evenodd"/>
  <text class="contact-text" x="80" y="1549">415 Harbor Street</text>
  <text class="contact-text" x="80" y="1572">Glenmont, Ohio 44628</text>

  <!-- contact: phone -->
  <path class="icon" d="M360,1544 l6,-3 l5,9 l-4,3 c2,5 6,9 11,11 l3,-4 l9,5 l-3,6 c-14,0 -27,-13 -27,-27 z"/>
  <text class="contact-text" x="397" y="1561">800-555-0142</text>

  <!-- contact: fax -->
  <rect class="icon" x="620" y="1548" width="15" height="6"/>
  <rect class="icon" x="620" y="1557" width="15" height="9"/>
  <rect class="icon" x="637" y="1548" width="6" height="18"/>
  <rect class="icon" x="645" y="1544" width="4" height="22"/>
  <rect class="icon" x="624" y="1544" width="11" height="3"/>
  <text class="contact-text" x="660" y="1561">800-555-0143</text>

  <!-- contact: web -->
  <circle class="icon-line" cx="821" cy="1555" r="13"/>
  <ellipse class="icon-line" cx="821" cy="1555" rx="6" ry="13"/>
  <line class="icon-line" x1="808" y1="1555" x2="834" y2="1555"/>
  <line class="icon-line" x1="810" y1="1548" x2="832" y2="1548"/>
  <line class="icon-line" x1="810" y1="1562" x2="832" y2="1562"/>
  <text class="contact-text" x="855" y="1561">www.CorvaneSystems.com</text>
</svg>
</body>
</html>
```